Hair dresser flyer for Air conditioning heat pumps A5

We require a flyer that is selling the benifits of air conditioning heat pumps which cools in summer and efficently heats in winter. Colour should be white background. Red and blue from logo to represent the Air conditioning Heat pump does heating and cooling and energy effient.

Target Market(s)

Hairdressor, Salons , barbers ,

Colors
0054AA
0677BA
7BADD7
CADEEF
E8F1F8
EB3D1F
EC4F4E
F09395
F8D3D4
FCEDEE

Requirements
Must have
• Cost from

```html
<!DOCTYPE html>
<html lang="en">
<head>
<meta charset="utf-8">
<title>Calder – Air Conditioning Heat Pump Flyer</title>
<link href="https://fonts.googleapis.com/css2?family=Anton&family=Oswald:wght@500;600&family=Open+Sans:wght@600;700&family=Noto+Sans:wght@400&display=swap" rel="stylesheet">
<style>
  :root {
    --backdrop: #b2a8a4;
    --coral: #ec4f4e;
    --flame: #e8501f;
    --sky: #36a9e1;
    --navy: #0054aa;
    --tick: #14298c;
    --ink: #111;
    --link-blue: #2a74d6;
    --link-red: #eb3d1f;
    --white: #fff;
  }
  * { margin: 0; padding: 0; box-sizing: border-box; }
  html, body { width: 1200px; height: 1200px; overflow: hidden; background: var(--backdrop); }
  .canvas { position: relative; width: 1200px; height: 1200px; }

  .flyer { position: absolute; width: 527px; height: 748px; background: var(--white); overflow: hidden; }
  .flyer--front { left: 73px; top: 134px; }
  .flyer--back { left: 625px; top: 336px; }

  /* Front */
  .headline {
    position: absolute; left: 0; top: 0; width: 100%; height: 172px; background: var(--coral);
    color: var(--white); font-family: "Anton", sans-serif; font-weight: 400; text-align: center;
    font-size: 38px; line-height: 45px; padding-top: 14px;
  }
  .headline .big { font-size: 46px; }

  .benefits { position: absolute; left: 17px; top: 196px; list-style: none; }
  .benefits li {
    display: flex; align-items: center; height: 24.7px; white-space: nowrap;
    font-family: "Oswald", sans-serif; font-weight: 600; font-size: 21px; color: var(--flame);
  }
  .benefits svg { width: 18px; height: 14px; margin-right: 9px; margin-top: 4px; flex: none; }

  .body-copy {
    position: absolute; left: 28px; top: 417px; width: 278px;
    font-family: "Oswald", sans-serif; font-weight: 500; font-size: 10.4px; line-height: 13.6px; color: var(--ink);
  }
  .body-copy p { margin-bottom: 13.6px; }

  .brand { position: absolute; display: flex; align-items: center; }
  .brand-square { background: var(--sky); flex: none; }
  .brand-name { font-family: "Oswald", sans-serif; font-weight: 600; color: var(--ink); }

  .brand--front { left: 36px; top: 654px; }
  .brand--front .brand-square { width: 12px; height: 12px; margin-right: 12px; }
  .brand--front .brand-name { font-size: 42px; line-height: 50px; }

  .price-tag {
    position: absolute; left: 324px; top: 176px; width: 203px; height: 89px; background: var(--flame);
    color: var(--white); font-family: "Open Sans", sans-serif; font-weight: 700; font-size: 15.5px; line-height: 21.3px;
    padding: 2px 0 0 19px;
  }
  .photo-column { position: absolute; left: 324px; top: 265px; width: 203px; height: 483px; }
  .photo-column svg { position: absolute; inset: 0; }
  .photo {
    position: absolute; left: 28px; width: 148px; height: 148px; border-radius: 50%;
    border: 4px solid var(--white);
  }
  .photo--1 { top: 8px; background: linear-gradient(160deg, #f2f2f2 0 30%, #2b2b2b 45%, #3a3a3a 80%, #cfcfcf); }
  .photo--2 { top: 164px; background: radial-gradient(circle at 50% 55%, #222 0 22%, #7a6f62 40%, #a89a88 100%); }
  .photo--3 { top: 324px; background: linear-gradient(170deg, #cdd3d8, #8f9aa3 55%, #c4b5ac); }

  /* Back */
  .top-band { position: absolute; left: 0; top: 0; width: 492px; height: 29px; background: var(--sky); }
  .side-strip { position: absolute; right: 0; top: 0; width: 35px; height: 100%; background: var(--flame); }
  .backdrop-photo {
    position: absolute; left: 0; top: 29px; width: 492px; height: 632px;
    background: linear-gradient(180deg, #f1eff1 0%, #eae6e8 30%, #f4eef0 48%, #e6e6e6 62%, #9c9c9c 82%, #d9d9d9 100%);
  }
  .brand--back { left: 27px; top: 66px; }
  .brand--back .brand-square { width: 14px; height: 14px; margin-right: 13px; }
  .brand--back .brand-name { font-size: 52px; line-height: 60px; }

  .savings-copy {
    position: absolute; left: 25px; top: 186px; white-space: nowrap;
    font-family: "Noto Sans", sans-serif; font-size: 17.4px; line-height: 21.7px; color: var(--ink); letter-spacing: 0.9px;
  }
  .example-box {
    position: absolute; left: 30px; top: 369px; width: 405px; height: 204px; border: 3px solid var(--ink);
    padding: 17px 0 0 16px; white-space: nowrap;
    font-family: "Oswald", sans-serif; font-weight: 600; font-size: 17.5px; line-height: 21.4px; color: var(--ink);
  }
  .example-box p { margin-bottom: 21px; }

  .contact-bar {
    position: absolute; left: 0; top: 661px; width: 492px; height: 87px; background: #000;
    padding: 8px 0 0 19px; white-space: nowrap;
    font-family: "Open Sans", sans-serif; font-weight: 600; font-size: 16.3px; line-height: 21.6px; color: var(--link-blue);
  }
  .contact-bar .phone { color: var(--white); }
  .contact-bar .web { color: var(--link-red); }
</style>
</head>
<body>
<div class="canvas">

  <section class="flyer flyer--front">
    <h1 class="headline"><span class="big">SAVE £££</span> on your Shops<br>Heating costs And stay Cool<br>in the Summer</h1>

    <ul class="benefits">
      <li><svg viewBox="0 0 18 14"><path d="M1 7 L6 12 L17 2" fill="none" stroke="var(--tick)" stroke-width="2"/></svg>Cools in Summer</li>
      <li><svg viewBox="0 0 18 14"><path d="M1 7 L6 12 L17 2" fill="none" stroke="var(--tick)" stroke-width="2"/></svg>Efficient Heats in Winter</li>
      <li><svg viewBox="0 0 18 14"><path d="M1 7 L6 12 L17 2" fill="none" stroke="var(--tick)" stroke-width="2"/></svg>More Productive staff</li>
      <li><svg viewBox="0 0 18 14"><path d="M1 7 L6 12 L17 2" fill="none" stroke="var(--tick)" stroke-width="2"/></svg>Increased Sales</li>
      <li><svg viewBox="0 0 18 14"><path d="M1 7 L6 12 L17 2" fill="none" stroke="var(--tick)" stroke-width="2"/></svg>Reduce cancellation in Summer</li>
      <li><svg viewBox="0 0 18 14"><path d="M1 7 L6 12 L17 2" fill="none" stroke="var(--tick)" stroke-width="2"/></svg>Filters and cleans the air</li>
      <li><svg viewBox="0 0 18 14"><path d="M1 7 L6 12 L17 2" fill="none" stroke="var(--tick)" stroke-width="2"/></svg>Reduced allergens &amp; Bugs</li>
      <li><svg viewBox="0 0 18 14"><path d="M1 7 L6 12 L17 2" fill="none" stroke="var(--tick)" stroke-width="2"/></svg>Reduce Humidity</li>
    </ul>

    <div class="body-copy">
      <p>Air Conditioning Heat Pumps creates the ideal environment all year round for staff to be at there most productive and for consumers to spend more time and, accordingly, more money.</p>
      <p>Modern Air Conditioning Heat pumps are one of the most energy efficient forms of heating available and ideal for those looking for a simple cost effective way to heat and cool the space. They are easy to install and operate and can quickly provide with the comfort you need.</p>
      <p>Reduce cancelations and absences in the warm summer months with Cooling mode. With the warms temperatures inside hairdressers and salons and clients not wanting to sit in somewhere with extreme heat,</p>
    </div>

    <div class="brand brand--front">
      <span class="brand-square"></span>
      <span class="brand-name">Calder</span>
    </div>

    <div class="price-tag">Energy- Efficient<br>Air Conditioning<br>Heat Pumps installed<br>from £1750 + Vat</div>

    <div class="photo-column">
      <svg viewBox="0 0 203 483" preserveAspectRatio="none" width="203" height="483">
        <rect width="203" height="483" fill="var(--sky)"/>
        <polygon points="178,0 203,0 203,483 11,483" fill="var(--navy)"/>
      </svg>
      <div class="photo photo--1" role="img" aria-label="Wall-mounted black air conditioning unit in a salon"></div>
      <div class="photo photo--2" role="img" aria-label="Ceiling cassette air conditioning unit installed in a shop"></div>
      <div class="photo photo--3" role="img" aria-label="Grey wall-mounted air conditioning unit"></div>
    </div>
  </section>

  <section class="flyer flyer--back">
    <div class="backdrop-photo" role="img" aria-label="Faded photo of a ceiling cassette unit above a floral salon display and a wall-mounted unit"></div>
    <div class="top-band"></div>
    <div class="side-strip"></div>

    <div class="brand brand--back">
      <span class="brand-square"></span>
      <span class="brand-name">Calder</span>
    </div>

    <p class="savings-copy">Reduce heating energy &nbsp;cost by up to 75% vs<br>electric heating. Air conditioning heat pumps is<br>a more efficient heating solution in comparison<br>to a standard electric heaters which are still<br>used in many businesses. This is because air<br>conditioning produces more heat for the<br>amount of electricity it takes to power the unit.</p>

    <div class="example-box">
      <p>Here's an example to illustrate how an air-to-air heat<br>pump can save you money over an electric &nbsp;heaters</p>
      <p>2 x 2kw Eleectic fan heaters<br>4kw Electricity input &nbsp;= &nbsp;4kw heat Output</p>
      <p>4kw Air Conditioning heat pump<br>1kw Electricty input = &nbsp;4kw Heat output</p>
    </div>

    <div class="contact-bar">
      If you are interested in having air conditioning installed<br>
      in your &nbsp;business, then give us a call on &nbsp;<span class="phone">01632 960481</span><br>
      or visit our website &nbsp;<span class="web">https://www.calderclimate.co/.</span>
    </div>
  </section>

</div>
</body>
</html>
```